Native Bush Healing Balms/Oils needs label/logo

Kōwhai Ripples is our name, we are a new startup business in New Zealand. Kōwhai means love in Maori. We make native bush balms, oils, tinctures, teas and do mirimiri which is a form of Maori healing. We are wanting a design for a balm label first off, however keep in mind that we will be wanting to transfer the logo across to other products, like the teas, t-shirts and even a calico tote bag! We would like it so we can edit the ingredients if possible.

We have had the 'flower/heart logo' made up to replace the 'o' in kōwhai. This we would like in a metallic electric purple/violet colour. We would like the 'kōwhai ripples' in silver. Please make sure the macron is above the last ā in kōwhai. We are open to other colour options and other styles of the flower/heart logo.

We would like the overall effect to be simple, clean, minimalist, bright. Colours we like are electric purple/violet, silver, then thinking of different colours for the different types/flavours, probably on a matte sticker. Fonts we think will suit are an italic curved/rounded font for the kōwhai and a capital font for the vibrations.

We have had a quick mock up of the labels which is attached. Also attached is a photo of my current balm and teas, and label ideas that I like. The drawings show a sticker for the lid with a safety tab.

Looking forward to seeing your wonderful designs! :)

Target Market(s)

People into natural self healing, who want traditionally made high vibrational, top end products

Industry/Entity Type

Health And Wellness

Requirements
Must have
• Silver writing on logo, or front of jar or lid.
• 'Made in Aotearoa' on jar
Nice to have
• Colours I like are hot pink, yellow, bright teal green, royal purple
Should not have
• Should not be cluttered

```html
<!DOCTYPE html>
<html lang="en">
<head>
<meta charset="utf-8">
<title>Kōwhai Ripples – Kawakawa Balm Labels</title>
<link rel="stylesheet" href="https://fonts.googleapis.com/css2?family=Nunito+Sans:wght@300;400&family=Teko:wght@400&display=swap">
<style>
  :root {
    --page: #ffffff;
    --label: #1f1d1e;
    --violet: #7d3fa0;
    --violet-soft: #8e4fb3;
    --silver: #c9c9cb;
    --silver-dim: #b3b3b5;
    --body-text: #d6d6d6;
    --leaf-green: #5cc58d;
  }
  * { box-sizing: border-box; margin: 0; padding: 0; }
  html, body {
    width: 1200px; height: 602px; overflow: hidden;
    background: var(--page);
    font-family: "Nunito Sans", Arial, sans-serif;
  }
  .sheet { position: relative; width: 1200px; height: 602px; }

  /* Lid stickers */
  .lid-tab {
    position: absolute; top: 120px; height: 96px;
    background: var(--label);
    display: flex; align-items: center; justify-content: center;
    color: var(--silver-dim); font-weight: 300; font-size: 18px;
    line-height: 1.25; text-align: center; text-transform: uppercase;
  }
  .lid-tab--brand { left: 240px; width: 218px; padding-left: 40px; }
  .lid-tab--symbol { left: 810px; width: 296px; padding-left: 60px; }
  .lid {
    position: absolute; top: 42px; width: 252px; height: 252px;
    border-radius: 50%; background: var(--label);
  }
  .lid--brand { left: 52px; }
  .lid--symbol { left: 622px; }
  .lid-ring {
    position: absolute; inset: 8px; border-radius: 50%;
    border: 4px solid var(--violet);
  }

  /* Wordmark */
  .wordmark {
    position: absolute; left: 0; right: 0; text-align: center;
    color: var(--silver); font-weight: 300;
  }
  .wordmark__name { display: block; line-height: 1; }
  .wordmark__sub {
    display: block; text-transform: uppercase; letter-spacing: 0.32em;
  }
  .lid--brand .wordmark { top: 82px; }
  .lid--brand .wordmark__name { font-size: 56px; }
  .lid--brand .wordmark__sub { font-size: 17px; margin-top: 8px; padding-left: 0.32em; }

  .lid--symbol .wordmark { top: 100px; }
  .lid--symbol .wordmark__name { font-size: 44px; }
  .lid--symbol .wordmark__sub { font-size: 14px; margin-top: 6px; padding-left: 0.32em; }

  /* Wrap band */
  .band {
    position: absolute; left: 55px; top: 310px; width: 1085px; height: 244px;
    background: var(--label);
  }
  .band .wordmark { left: 60px; right: auto; width: 450px; top: 28px; }
  .band .wordmark__name { font-size: 70px; }
  .band .wordmark__sub { font-size: 21px; margin-top: 10px; padding-left: 0.32em; }

  .product-name {
    position: absolute; left: 60px; width: 450px; top: 138px;
    text-align: center; font-family: "Teko", "Arial Narrow", sans-serif;
    font-size: 38px; letter-spacing: 0.06em; color: var(--leaf-green); line-height: 1;
  }
  .divider-ornament {
    position: absolute; left: 225px; top: 186px; width: 120px; height: 8px;
    background: linear-gradient(90deg, transparent, var(--violet) 20%, var(--violet) 80%, transparent);
    border-radius: 4px;
  }
  .product-type {
    position: absolute; left: 60px; width: 450px; top: 205px;
    text-align: center; font-size: 13px; letter-spacing: 0.22em;
    color: var(--silver-dim); font-weight: 300;
  }
  .pattern-strip {
    position: absolute; left: 519px; top: 4px; width: 36px; height: 236px;
    background: linear-gradient(180deg, var(--violet), var(--violet-soft), var(--violet));
    border-radius: 6px; opacity: 0.85;
  }

  .details {
    position: absolute; left: 639px; top: 18px; width: 420px;
    color: var(--body-text); font-size: 16.5px; line-height: 1.45; font-weight: 300;
  }
  .details p + p { margin-top: 21px; }
  .details .volume { margin-top: 16px; }
  .details .footer {
    margin-top: 14px; display: flex; align-items: center;
  }
  .social-dot {
    width: 24px; height: 24px; border-radius: 50%;
    background: var(--violet); margin-right: 9px; flex: none;
  }
  .origin { margin-left: 40px; }
</style>
</head>
<body>
<main class="sheet">

  <!-- Lid sticker with wordmark -->
  <div class="lid-tab lid-tab--brand">Heal the<br>people</div>
  <div class="lid lid--brand">
    <div class="lid-ring"></div>
    <div class="wordmark">
      <span class="wordmark__name">kōwhai</span>
      <span class="wordmark__sub">ripples</span>
    </div>
  </div>

  <!-- Lid sticker with name in place of symbol -->
  <div class="lid-tab lid-tab--symbol">Heal the<br>people</div>
  <div class="lid lid--symbol">
    <div class="wordmark">
      <span class="wordmark__name">kōwhai</span>
      <span class="wordmark__sub">ripples</span>
    </div>
  </div>

  <!-- Jar wrap band -->
  <section class="band">
    <div class="wordmark">
      <span class="wordmark__name">kōwhai</span>
      <span class="wordmark__sub">ripples</span>
    </div>
    <h1 class="product-name">KAWAKAWA</h1>
    <div class="divider-ornament" role="img" aria-label="Small violet flourish divider"></div>
    <p class="product-type">HANDMADE BALM</p>

    <div class="pattern-strip" role="img" aria-label="Vertical chain of violet spiral koru ornaments"></div>

    <div class="details">
      <p>I’m great on minor skin irritation, cuts, bites, rashes etc. Rub me in lovingly, little and often.</p>
      <p>Made with kavakia, sacred sounds and traditional knowledge from kawakawa,oil, beeswax and kōwhai.</p>
      <p class="volume">15 ml</p>
      <div class="footer">
        <span class="social-dot"></span>
        <span>kōwhairipples</span>
        <span class="origin">Made in Aotearoa</span>
      </div>
    </div>
  </section>

</main>
</body>
</html>
```